International Fleet Management Firm Website

HaulvergeKenda is a Fleet Management Company that provides insight into customers fleets. We do this through web tools which we have developed which function through a client login screen to help ensure that corporates are able to stay on top of their fleets 24/7.
We are about to launch and are looking for a great new website to help us come out with bang! We would like a site that matches our values of ; Courage, integrity and leadership.
Although we have developed the app. We would also like to redesign the look of the site on the back end.
(1) We need to incorporate the new corporate colours
(2) Would like to create a better user experience.
The site that I would like to model ours after is;
www.brellix.com (usa version)
Good Luck!!
Updates
Jusst added the .png version of the logo. Hopes this helps!
Industry/Entity Type
It Company
Look and feel

```html
<!DOCTYPE html>
<html lang="en">
<head>
<meta charset="utf-8">
<title>HaulvergeKenda — Fleet Management</title>
<link href="https://fonts.googleapis.com/css2?family=Open+Sans:wght@400;600;700&family=PT+Sans+Narrow:wght@700&family=Questrial&family=Roboto+Condensed:wght@700&display=swap" rel="stylesheet">
<style>
:root{
  --red:#8e2628;
  --red-btn:#9a2a2a;
  --blue:#2a8dbd;
  --blue-dark:#1f6f98;
  --ink:#2b2b2b;
  --card:#f4f6f8;
  --light:#e6e7e8;
  --footer:#3e3f40;
  --footer-line:#2c2d2e;
  --bar:#555657;
  --white:#fff;
}
*{box-sizing:border-box;margin:0;padding:0}
html,body{width:1080px;height:1200px;overflow:hidden;background:var(--light)}
body{position:relative;font-family:"Questrial",sans-serif;color:var(--ink)}
.abs{position:absolute}

.topbar{left:0;top:0;width:1080px;height:106px;background:var(--red)}
.navbar{left:0;top:106px;width:1080px;height:34px;background:var(--blue)}
.nav a{position:absolute;top:117px;font:11.5px Arial,sans-serif;color:var(--white);text-decoration:none;white-space:nowrap}

.brand{left:104px;top:0;width:222px;height:152px}
.brand-name{left:112px;top:80px;width:206px;display:flex;align-items:center;justify-content:center;gap:6px;font:700 21px "Open Sans",sans-serif;color:var(--blue-dark);letter-spacing:-.3px}
.brand-name i{display:block;width:12px;height:12px;background:var(--blue-dark)}
.tagline{left:104px;top:117px;width:222px;text-align:center;font:9px "Questrial",sans-serif;letter-spacing:2px;color:#555}

.login{top:10px;height:32px;border-radius:4px;background:linear-gradient(#3aa3d6,#1f7fb0);border:1px solid #15628a;color:#0e4766;font:700 12px Arial,sans-serif;display:flex;align-items:center;padding-left:12px}
.login span{margin-left:auto;width:30px;height:100%;border-left:1px solid #15628a;display:flex;align-items:center;justify-content:center}
.call{right:112px;top:60px;font:700 27px "Roboto Condensed",sans-serif;color:var(--white)}

.hero{left:0;top:140px;width:1080px;height:502px;background:linear-gradient(180deg,#8fb6d8 0%,#c6dcea 35%,#b6a98a 60%,#e4d8c2 100%)}
.headline{font:700 27px "PT Sans Narrow",sans-serif;color:var(--white);text-shadow:1px 1px 2px rgba(0,0,0,.5);white-space:nowrap}

.card{top:470px;width:288px;height:141px;background:var(--card);padding:6px 11px}
.card h3{font:600 19px "Open Sans",sans-serif;color:var(--blue);white-space:nowrap}
.card p{margin-top:6px;font:10px/13.6px "Questrial",sans-serif;color:#333}
.card .more{position:absolute;right:22px;bottom:14px;font:8.5px Arial,sans-serif;color:#c0392b}

.info{top:642px;left:0;width:1080px;height:309px;background:linear-gradient(180deg,#9ccbe2 0%,#e2e4e6 22%,#e6e7e8 100%)}
.section h2{font:700 29px "Open Sans",sans-serif;color:var(--blue);letter-spacing:.3px;white-space:nowrap}
.section p{margin-top:14px;font:12.3px/14.4px "Questrial",sans-serif;color:#222}
.btn{height:28px;width:78px;background:var(--red-btn);color:var(--white);font:8.5px Arial,sans-serif;display:flex;align-items:center;justify-content:center;gap:4px}
.btn b{color:#f2c200}

.footer{left:0;top:951px;width:1080px;height:218px;background:var(--footer)}
.footer-title{top:961px;font:700 21px "Open Sans",sans-serif;color:var(--blue)}
.links{left:119px;top:995px;list-style:none}
.links li{font:11.5px/20.8px Arial,sans-serif;color:var(--white)}
.vline{top:996px;width:1px;height:146px;background:var(--footer-line)}
.field{left:381px;width:200px;height:28px;background:#505253;border:1px solid #6a6c6d;color:#ddd;font:10px Arial,sans-serif;padding:8px 12px}
.submit{left:381px;top:1078px;width:200px;height:28px;background:var(--red);border:1px solid #b44;color:var(--white);font:700 13px "Open Sans",sans-serif;text-align:center;line-height:26px}
.contact-box{left:745px;top:997px;width:223px;height:33px;background:#d7d8d9;display:flex;align-items:center;gap:6px;padding-left:10px;font:700 20px "Open Sans",sans-serif;color:var(--blue-dark)}
.contact-box i{width:14px;height:14px;background:var(--blue-dark)}
.row{left:745px;display:flex;align-items:flex-start;gap:8px;font:10px/13px Arial,sans-serif;color:var(--white)}
.row svg{flex:none}
.bottombar{left:0;top:1169px;width:1080px;height:31px;background:var(--bar);text-align:center;font:9px/31px Arial,sans-serif;color:#ddd;letter-spacing:.3px}
</style>
</head>
<body>

<div class="abs topbar"></div>
<div class="abs navbar"></div>

<svg class="abs brand" viewBox="0 0 222 152" aria-hidden="true">
  <path d="M1 0H221V135L111 151L1 135Z" fill="#fff" stroke="#d8d8d8"/>
</svg>
<div class="abs brand-name"><i></i>HaulvergeKenda</div>
<div class="abs tagline">Clarity for Every Route</div>

<div class="abs login" style="left:702px;width:135px">Client Login<span><svg width="18" height="18" viewBox="0 0 18 18"><circle cx="9" cy="9" r="8" fill="#123c55"/><path d="M5 9h7M9 5.5 12.5 9 9 12.5" stroke="#fff" stroke-width="1.8" fill="none"/></svg></span></div>
<div class="abs login" style="left:847px;width:120px">Driver Login<span><svg width="18" height="18" viewBox="0 0 18 18"><circle cx="9" cy="9" r="8" fill="#123c55"/><path d="M5 9h7M9 5.5 12.5 9 9 12.5" stroke="#fff" stroke-width="1.8" fill="none"/></svg></span></div>
<div class="abs call">Call 24/7 (555) 210 XXXX</div>

<nav class="nav">
  <a style="left:358px">HOME</a>
  <a style="left:422px">ABOUT US</a>
  <a style="left:510px">OUR SERVICES</a>
  <a style="left:626px">FLEET SOLUTION</a>
  <a style="left:751px">RESOURCE CENTER</a>
  <a style="left:895px">CONTACT US</a>
</nav>

<div class="abs hero" role="img" aria-label="Photograph of a fleet of vehicles — a red box truck, a red sedan, a white semi truck, a silver pickup and a white van — parked on a sandy beach beside the sea and a rocky cliff"></div>
<div class="abs headline" style="left:266px;top:158px">Running an efficient fleet positively affects</div>
<div class="abs headline" style="right:112px;top:190px">the profitability of your organization</div>

<div class="abs card" style="left:104px">
  <h3>Strategic Fleet Management</h3>
  <p>Regardless of you industry, company or individual circumstance, HVK can help you achieve your Fleet Targets. Our team of professionals can help you run an optimal fleet using HVK 2.0 our in house Fleet Management Software.</p>
  <span class="more">Learn more ⁜</span>
</div>
<div class="abs card" style="left:400px">
  <h3>Total Cost Management</h3>
  <p>Costs are an ongoing challenge which needs to be constantly managed. Every decision taken has long term effects on your success. As your partner, HVK works with you to ensure that these costs stay under control all the time.</p>
  <span class="more">Learn more ⁜</span>
</div>
<div class="abs card" style="left:695px">
  <h3>Fuel Management</h3>
  <p>Regardless of you industry, company or individual circumstance, HVK can help you achieve your Fleet Targets. Our team of professionals can help you run an optimal fleet using HVK 2.0 our in house Fleet Management Software.</p>
  <span class="more">Learn more ⁜</span>
</div>

<div class="abs info"></div>
<section class="abs section" style="left:121px;top:688px;width:410px">
  <h2>WHO WE ARE</h2>
  <p>HVK was formed to fill a need in the Fleet Management Industry. We aim to provide first class Fleet Management Services to organizations. Whether your fleet is owned, outsourced or a mixture – we aim to help you ensure that your costs stay controlled.</p>
  <p>We also advise clients on vehicles and processes that will help improve your bottom line.</p>
  <p>We provide organizations with company cars and trucks along with unmatched service and support.</p>
</section>
<div class="abs btn" style="left:450px;top:906px">Learn more <b>➔</b></div>

<section class="abs section" style="left:560px;top:688px;width:410px">
  <h2>FLEET ADMINISTRATION</h2>
  <p>When it comes to choosing your fleet management partner, you want a leader with the experience and expertise to handle the many complexities. You want easy to use tools that provide rich data and insights. Mostly, you want reassurance that your fleet will run well on a day-to-day basis without you getting bogged down with the details. With HVK, you get exactly all this...and so much more.</p>
  <p>We provide organizations with company cars and trucks along with unmatched service and support.</p>
</section>
<div class="abs btn" style="left:890px;top:906px">Learn more <b>➔</b></div>

<footer class="abs footer"></footer>
<h4 class="abs footer-title" style="left:118px">Brows site</h4>
<h4 class="abs footer-title" style="left:410px">Let us call you</h4>
<h4 class="abs footer-title" style="left:745px">Contact info</h4>

<ul class="abs links">
  <li>Home</li><li>About Us</li><li>Our services</li><li>Fleet Solution</li><li>Resource Center</li><li>Contact us</li>
</ul>
<div class="abs vline" style="left:296px"></div>
<div class="abs vline" style="left:662px"></div>

<div class="abs field" style="top:997px">Enter your name</div>
<div class="abs field" style="top:1037px">Enter your email address</div>
<div class="abs submit">Submit</div>

<div class="abs contact-box"><i></i>HaulvergeKenda</div>
<div class="abs row" style="top:1044px">
  <svg width="14" height="18" viewBox="0 0 14 18"><path d="M7 1a6 6 0 0 1 6 6c0 4-6 10-6 10S1 11 1 7a6 6 0 0 1 6-6z" fill="#bbb"/><circle cx="7" cy="7" r="2.3" fill="#3e3f40"/></svg>
  <span>Lorem Ipsum. Proin gravida nibh vel<br>velit auctor aliquet. Aenean</span>
</div>
<div class="abs row" style="top:1082px">
  <svg width="12" height="16" viewBox="0 0 12 16"><rect x="1" y="0.5" width="10" height="15" rx="1.5" fill="#bbb"/><rect x="2.5" y="2.5" width="7" height="9" fill="#3e3f40"/></svg>
  <span style="line-height:16px">(555) 210 XXXX</span>
</div>
<div class="abs row" style="top:1112px">
  <svg width="14" height="14" viewBox="0 0 14 14"><rect x="3" y="0.5" width="8" height="4" fill="#bbb"/><rect x="0.5" y="4.5" width="13" height="6" rx="1" fill="#bbb"/><rect x="3" y="9" width="8" height="4.5" fill="#ddd"/></svg>
  <span style="line-height:14px">(555) 210 XXXX</span>
</div>
<div class="abs row" style="top:1140px">
  <svg width="14" height="12" viewBox="0 0 14 12"><path d="M1 4 7 0l6 4v7.5H1z" fill="#bbb"/><path d="M1 4l6 4 6-4" stroke="#3e3f40" fill="none"/></svg>
  <span style="line-height:12px">info@haulvergekenda.com</span>
</div>

<div class="abs bottombar">(c) 2013. HaulvergeKenda, All Rights Reserved.</div>

</body>
</html>
```